Private Maths Tuition Flyer based in London

I am opening up a new Maths tuition centre in North West London. The flyer will be delivered to over 8,000 homes within the immediate vicinity. The design should be suitable to be printed on an A5 sheet and read in a portrait orientation.

The flyer should include the following:

The headline statement should be "Private Maths Tuition"

Secondary headline statement is the following "GCSE, A-Levels, 11 Plus exams"

Some of service offerings/selling points are:

- Free first session
- Monthly Feedback reports
- Free support outside of sessions
- Clear Target grades
- Personalised Lesson plans
- Tangible Results

Another statement that should be featured is "Book your free session by visiting www.lernova.co.uk" or something similar to that.

"Contact Details:
020 4719 8263
enquiries@lernova.co.uk"

"Address:
Kelbridge Business and Innovation Centre
Ashvale Court
Wrenfield Road
HA4 9QD"

Attached you'll see a logo which should be included and also a map of where we are. I am open to new images for the map if you guys have any, rather than a screen shot from google maps but it should be clear to see.

I would like the content above to be displayed in a clear and concise manner that is easy to read. You have creative license on where this information should be displayed and where the images should be but on the whole it should look aesthetically pleasing on the eye.

Target Market(s)

Students, Parents. Parents who want maths tutors.

Industry/Entity Type

Tutoring

Font styles to use
Sans Serif

Requirements
Must have
• *logo*
• Private Maths Tuition
• GCSE, A-Levels, 11 Plus exams
• - Free first session
• - Monthly Feedback reports
• - Free support outside of sessions
• - Clear Target grades
• - Personalised Lesson plans
• - Tangible Results
• Book your free session by visiting www.lernova.co.uk" or something similar to that.
• Contact Details:
• 020 4719 8263
• enquiries@lernova.co.uk
• Address (*with map*):
• Kelbridge Business and Innovation Centre
• Ashvale Court
• Wrenfield Road
• HA4 9QD
Nice to have
• similar colour scheme as the logo. creative background design.

```html
<!DOCTYPE html>
<html lang="en">
<head>
<meta charset="utf-8">
<title>Lernova – Private Math Tuition Flyer</title>
<link rel="stylesheet" href="https://fonts.googleapis.com/css2?family=Raleway:wght@700;800&family=Roboto:wght@400;500&display=swap">
<style>
  :root {
    --navy: #252b36;
    --navy-deep: #1f242e;
    --green: #5aa532;
    --green-light: #8cc63f;
    --green-band: #4a9a2c;
    --paper: #f4f4f4;
    --white: #ffffff;
    --ink: #3a3f47;
    --muted: #c9cdd3;
    --orange: #e8571e;
  }
  * { margin: 0; padding: 0; box-sizing: border-box; }
  html, body { width: 923px; height: 1200px; overflow: hidden; background: var(--white); }
  .flyer {
    position: relative; width: 923px; height: 1200px; overflow: hidden;
    font-family: 'Roboto', Arial, sans-serif; color: var(--ink);
  }
  .backdrop { position: absolute; inset: 0; }
  .brand {
    position: absolute; left: 96px; top: 50px;
    display: flex; align-items: center; gap: 10px;
    font-family: 'Roboto', Arial, sans-serif; font-weight: 500;
    font-size: 34px; color: var(--orange);
  }
  .brand-dot { width: 16px; height: 16px; border-radius: 50%; background: var(--green); }
  .site-tag {
    position: absolute; left: 679px; top: 46px; width: 183px; height: 31px;
    border: 1.5px solid #9a9ea5; font-size: 14.5px; color: #555;
    display: flex; align-items: center; justify-content: center;
  }
  .hero-title {
    position: absolute; left: 78px; top: 196px; color: var(--white);
    font-family: 'Raleway', Arial, sans-serif; font-weight: 800; line-height: 1;
  }
  .hero-title .line-small { display: block; font-size: 42px; letter-spacing: 0.5px; }
  .hero-title .line-large { display: block; font-size: 80px; margin-top: 8px; letter-spacing: 1px; }
  .hero-sub {
    position: absolute; left: 79px; top: 338px; color: var(--white);
    font-size: 22px;
  }
  .hero-photo {
    position: absolute; left: 470px; top: 150px; width: 400px; height: 361px;
    border-radius: 200px 200px 0 0;
    background: radial-gradient(ellipse at 50% 35%, #c99a7a 0%, #8a5a45 35%, #d9266e 70%, #3b2a2f 100%);
  }
  .services-title {
    position: absolute; left: 0; right: 0; top: 552px; text-align: center;
    font-size: 25px; color: #333; letter-spacing: 0.3px;
  }
  .services-title strong { color: var(--green); font-weight: 500; }
  .service-list { position: absolute; top: 626px; list-style: none; }
  .service-list.left { left: 86px; }
  .service-list.right { left: 534px; }
  .service-item {
    display: flex; align-items: center; gap: 17px;
    height: 42px; font-size: 21px; color: #555;
  }
  .service-item svg { width: 32px; height: 32px; flex: none; }
  .booking {
    position: absolute; left: 0; right: 0; top: 848px; text-align: center;
    color: var(--white); font-size: 27px;
  }
  .map-panel {
    position: absolute; left: 61px; top: 959px; width: 400px; height: 187px;
    border-radius: 16px;
    background: linear-gradient(135deg, #dcd9d2 0%, #e6e3dc 45%, #a9c98a 75%, #dcd9d2 100%);
  }
  .contact { position: absolute; left: 502px; top: 960px; color: var(--muted); }
  .contact-title { font-size: 19px; color: var(--white); font-weight: 500; margin-bottom: 18px; }
  .contact-title span { color: var(--green-light); }
  .contact-address { font-style: normal; font-size: 17px; line-height: 22.5px; }
  .contact-lines {
    position: absolute; left: 502px; top: 1128px;
    display: flex; gap: 22px; font-size: 16.5px; color: var(--muted);
  }
  .contact-lines span { display: flex; align-items: center; gap: 7px; }
  .contact-lines svg { width: 14px; height: 14px; fill: var(--muted); }
</style>
</head>
<body>
<main class="flyer">
  <svg class="backdrop" width="923" height="1200" viewBox="0 0 923 1200" aria-hidden="true">
    <rect x="0" y="0" width="923" height="127" fill="var(--paper)"/>
    <rect x="0" y="127" width="923" height="460" fill="var(--green)"/>
    <path d="M923 127 L900 127 C885 270 820 360 700 410 L923 470 Z" fill="var(--green-light)"/>
    <path d="M0 127 H870 C855 270 770 370 640 420 C420 470 200 455 0 410 Z" fill="var(--navy)"/>
    <path d="M0 580 C180 530 380 511 923 511 V813 H0 Z" fill="var(--paper)"/>
    <rect x="0" y="813" width="923" height="110" fill="var(--green-band)"/>
    <path d="M330 813 C600 805 800 780 923 735 V813 Z" fill="var(--green-light)"/>
    <rect x="0" y="918" width="923" height="282" fill="var(--navy-deep)"/>
    <path d="M470 918 C690 928 850 955 923 1000 V918 Z" fill="var(--green)"/>
    <rect x="0" y="1185" width="923" height="15" fill="var(--green-light)"/>
  </svg>

  <header>
    <div class="brand"><span class="brand-dot"></span>Lernova</div>
    <div class="site-tag">www.lernova.co.uk</div>
  </header>

  <section class="hero">
    <h1 class="hero-title">
      <span class="line-small">PRIVATE MATH</span>
      <span class="line-large">TUITION</span>
    </h1>
    <p class="hero-sub">GCSE, A-Levels, 11 Plus exams</p>
    <div class="hero-photo" role="img" aria-label="Photo of a smiling schoolgirl with a colourful headband and scarf"></div>
  </section>

  <section class="services">
    <h2 class="services-title">OUR <strong>SERVICE</strong></h2>
    <ul class="service-list left">
      <li class="service-item"><svg viewBox="0 0 32 32"><circle cx="16" cy="16" r="14" fill="var(--green)"/><path d="M9 16.5l5 5 9-10" stroke="#fff" stroke-width="3" fill="none"/></svg>Free first session</li>
      <li class="service-item"><svg viewBox="0 0 32 32"><circle cx="16" cy="16" r="14" fill="var(--green)"/><path d="M9 16.5l5 5 9-10" stroke="#fff" stroke-width="3" fill="none"/></svg>Monthly Feedback reports</li>
      <li class="service-item"><svg viewBox="0 0 32 32"><circle cx="16" cy="16" r="14" fill="var(--green)"/><path d="M9 16.5l5 5 9-10" stroke="#fff" stroke-width="3" fill="none"/></svg>Free support outside of sessions</li>
    </ul>
    <ul class="service-list right">
      <li class="service-item"><svg viewBox="0 0 32 32"><circle cx="16" cy="16" r="14" fill="var(--green)"/><path d="M9 16.5l5 5 9-10" stroke="#fff" stroke-width="3" fill="none"/></svg>Clear Target grades</li>
      <li class="service-item"><svg viewBox="0 0 32 32"><circle cx="16" cy="16" r="14" fill="var(--green)"/><path d="M9 16.5l5 5 9-10" stroke="#fff" stroke-width="3" fill="none"/></svg>Personalised Lesson plans</li>
      <li class="service-item"><svg viewBox="0 0 32 32"><circle cx="16" cy="16" r="14" fill="var(--green)"/><path d="M9 16.5l5 5 9-10" stroke="#fff" stroke-width="3" fill="none"/></svg>Tangible Results</li>
    </ul>
  </section>

  <p class="booking">Book your free session by visiting www.lernova.co.uk</p>

  <footer>
    <div class="map-panel" role="img" aria-label="Street map showing the location of Kelbridge Business and Innovation Centre"></div>
    <div class="contact">
      <h3 class="contact-title">CONTACT <span>US</span></h3>
      <address class="contact-address">
        Kelbridge Business and Innovation Centre<br>
        Ashvale Court<br>
        Wrenfield Road<br>
        HA4 9QD
      </address>
    </div>
    <div class="contact-lines">
      <span><svg viewBox="0 0 16 16"><path d="M3 1h3l1.5 4-2 1.5a9 9 0 0 0 4 4L11 8.5l4 1.5v3a2 2 0 0 1-2 2A12 12 0 0 1 1 3a2 2 0 0 1 2-2z"/></svg>020 4719 8263</span>
      <span><svg viewBox="0 0 16 16"><path d="M1 3h14v10H1z M1.5 3.5l6.5 5 6.5-5" stroke="#1f242e" stroke-width="1.2"/></svg>enquiries@lernova.co.uk</span>
    </div>
  </footer>
</main>
</body>
</html>
```